We need a brand new Employee Handbook for a team of aged and disability support workers

We need an employee handbook designed for our team of aged and disability support workers.
We provide a range of disability and aged care services to persons in our region.
We are a small business, providing unique and personalised support to vulnerable people. We actually provide choice and control to our clients - something the bigger agencies say they do but don't follow through with.
We aim to be an employer of choice - providing a workplace that supports our staff personally and professionally.
We would like to see the colours gold, yellow, black, grey and white.
We would like to incorporate photos of our current team members and stock photos of fun teams, persons with a disability, elderly and carers in the community and home.
The final design should communicate a fun, supportive team offering growth and opportunity.

```html
<!DOCTYPE html>
<html lang="en">
<head>
<meta charset="utf-8">
<title>Marlowe Care – Induction Guide</title>
<link rel="stylesheet" href="https://fonts.googleapis.com/css2?family=Archivo+Black&family=Arimo:wght@400;700&display=swap">
<style>
:root{
  --bg:#d8d8da;
  --paper:#ffffff;
  --paper-soft:#f2f2f2;
  --ink:#1f1f1f;
  --title:#464646;
  --grey:#8d8d8d;
  --grey-bar:#6f6f6f;
  --gold:#c8ad3a;
  --gold-light:#e6d27a;
  --gold-dark:#a88f25;
}
*{box-sizing:border-box;margin:0;padding:0}
html,body{width:1200px;height:2317px;overflow:hidden}
body{background:var(--bg);font-family:"Arimo",Arial,sans-serif;color:var(--ink);position:relative}
.band{position:absolute;left:0;width:1200px}
.band-covers{top:0;height:612px}
.band-welcome{top:612px;height:517px;background:#dcdcde}
.band-pledge{top:1129px;height:576px}
.band-back{top:1705px;height:612px;background:#e1e1e3}

.spread{position:absolute;left:100px;display:flex;box-shadow:0 18px 40px rgba(0,0,0,.18)}
.page{position:relative;width:500px;height:360px;background:var(--paper);overflow:hidden}
.page + .page{border-left:1px solid #e4e4e4}

/* cover */
.cover{position:absolute;width:500px;height:360px;background:var(--paper);overflow:hidden;box-shadow:0 12px 28px rgba(0,0,0,.16)}
.cover-photo{position:absolute;right:0;top:0;width:205px;height:360px;
  background:linear-gradient(160deg,#d9a65a 0%,#e6c3a4 30%,#c98f7c 55%,#e26a6a 75%,#9fa9bb 100%)}
.cover-photo-top{position:absolute;right:205px;top:0;width:70px;height:90px;background:linear-gradient(180deg,#9aa6b8,#c7ced9)}
.brand{position:absolute;font-family:"Arimo",Arial,sans-serif;font-weight:700;color:var(--gold);white-space:nowrap;display:flex;align-items:center;gap:6px}
.brand-dot{width:9px;height:9px;border-radius:50%;background:var(--gold)}
.cover .brand{left:44px;top:44px;font-size:22px}
.cover-title{position:absolute;left:40px;top:100px;font-family:"Archivo Black",Arial,sans-serif;font-size:54px;line-height:.98;color:var(--title)}
.pill{position:absolute;border-radius:999px;background:linear-gradient(90deg,var(--gold-dark),var(--gold-light) 60%,var(--gold));color:var(--ink);display:flex;align-items:center}
.cover .pill{left:58px;top:252px;width:240px;height:40px;padding:0 16px;font-size:11px;line-height:1.2;justify-content:space-between}

.covers-stack{position:absolute;left:0;top:0;width:1200px;height:612px}
.covers-stack .c1{left:150px;top:170px}
.covers-stack .c2{left:290px;top:130px}
.covers-stack .c3{left:430px;top:90px;transform:scale(1.12);transform-origin:left top}

/* welcome */
.welcome-title{position:absolute;left:50px;top:170px;font-family:"Archivo Black",Arial,sans-serif;font-size:64px;color:var(--ink)}
.welcome .pill{left:52px;top:248px;height:24px;padding:0 18px;font-size:10px;font-weight:700;letter-spacing:.3px}
.welcome-circle{position:absolute;left:330px;top:40px;width:130px;height:130px;border-radius:50%;background:radial-gradient(circle at 50% 40%,#9fd6f0,#2d8fd0 70%,#1d6ea8)}
.acknowledge{position:absolute;left:40px;bottom:24px;right:30px;font-size:7px;font-weight:700}
.toc-photo{position:absolute;left:0;top:0;width:230px;height:360px;background:linear-gradient(150deg,#3a3633,#6b4a30 45%,#a97a4c 70%,#d9d4cc)}
.toc{position:absolute;left:252px;top:38px;right:20px}
.toc-title{font-family:"Arimo",Arial,sans-serif;font-weight:400;color:var(--grey);font-size:30px;line-height:.95;letter-spacing:.5px}
.toc-title b{display:block;font-size:36px}
.toc-rule{width:44px;height:3px;background:var(--title);margin:6px 0 12px}
.toc ol{list-style:none;font-size:7.5px;line-height:1.6;color:var(--ink)}
.toc ol span{display:inline-block;width:18px}
.toc ul{list-style:none;padding-left:50px;font-size:7px;line-height:1.5}

/* pledge */
.pledge-text{position:absolute;left:38px;top:60px;width:200px}
.pledge-text h2{font-size:20px;font-weight:400;line-height:1.1}
.pledge-text h2 strong{display:block;font-family:"Archivo Black",Arial,sans-serif;font-weight:400;font-size:19px}
.pledge-text p{font-size:7.5px;font-weight:700;line-height:1.35;margin-top:8px}
.pledge-photo{position:absolute;right:0;top:0;width:240px;height:320px;background:linear-gradient(160deg,#e8e2d8,#c7a98a 40%,#8a8f9c 70%,#d4bfa0)}
.footer-bar{position:absolute;left:0;bottom:18px;height:14px;background:var(--grey-bar);color:#fff;font-size:7px;display:flex;align-items:center;padding-left:24px}
.page-left .footer-bar{width:300px}
.page-right .footer-bar{width:100%}
.director-photo{position:absolute;left:40px;top:50px;width:140px;height:150px;border:4px solid #fff;outline:1px solid #bbb;background:linear-gradient(160deg,#e0e0e0,#7d7d7d 60%,#3b3b3b)}
.director .pill{left:50px;top:214px;width:120px;height:20px;justify-content:center;font-size:8px;font-weight:700}
.director-role{position:absolute;left:50px;top:240px;width:120px;text-align:center;font-size:7px;line-height:1.3;color:#555}
.director-msg{position:absolute;left:210px;top:40px;right:26px}
.director-msg h2{font-family:"Archivo Black",Arial,sans-serif;font-weight:400;color:var(--gold);font-size:18px;line-height:1.05}
.director-msg .lead{font-size:10.5px;line-height:1.25;margin-top:8px}
.director-msg .small{font-size:6.5px;line-height:1.35;margin-top:8px}
.page-tag{position:absolute;right:0;top:230px;width:30px;height:12px;background:var(--grey-bar);color:#fff;font-size:6px;text-align:center;line-height:12px}

/* back cover */
.back .brand{left:50%;top:200px;transform:translateX(-50%);font-size:22px}
.contacts{position:absolute;left:0;right:0;top:250px;display:flex;justify-content:center;flex-wrap:wrap;gap:6px 14px;font-size:8px;color:#333}
.contacts span{display:flex;align-items:center;gap:4px}
.contacts svg{width:9px;height:9px}
</style>
</head>
<body>

<section class="band band-covers">
  <div class="covers-stack">
    <div class="cover c1">
      <div class="cover-photo" role="img" aria-label="Team members stacking hands together"></div>
      <div class="cover-photo-top" role="img" aria-label="Team photo detail"></div>
      <div class="brand"><span class="brand-dot"></span>Marlowe Care</div>
      <h1 class="cover-title">Induction<br>Guide</h1>
      <div class="pill"><span>A practical guide to your<br>employment journey</span><svg width="34" height="10" viewBox="0 0 34 10"><path d="M0 5H31M26 1l5 4-5 4" stroke="#1f1f1f" stroke-width="1.4" fill="none"/></svg></div>
    </div>
    <div class="cover c2">
      <div class="cover-photo" role="img" aria-label="Team members stacking hands together"></div>
      <div class="cover-photo-top" role="img" aria-label="Team photo detail"></div>
      <div class="brand"><span class="brand-dot"></span>Marlowe Care</div>
      <h1 class="cover-title">Induction<br>Guide</h1>
      <div class="pill"><span>A practical guide to your<br>employment journey</span><svg width="34" height="10" viewBox="0 0 34 10"><path d="M0 5H31M26 1l5 4-5 4" stroke="#1f1f1f" stroke-width="1.4" fill="none"/></svg></div>
    </div>
    <div class="cover c3">
      <div class="cover-photo" role="img" aria-label="Team members stacking hands together"></div>
      <div class="cover-photo-top" role="img" aria-label="Team photo detail"></div>
      <div class="brand"><span class="brand-dot"></span>Marlowe Care</div>
      <h1 class="cover-title">Induction<br>Guide</h1>
      <div class="pill"><span>A practical guide to your<br>employment journey</span><svg width="34" height="10" viewBox="0 0 34 10"><path d="M0 5H31M26 1l5 4-5 4" stroke="#1f1f1f" stroke-width="1.4" fill="none"/></svg></div>
    </div>
  </div>
</section>

<section class="band band-welcome">
  <div class="spread" style="top:78px">
    <div class="page welcome">
      <div class="welcome-circle" role="img" aria-label="Smiling older man in a green jumper"></div>
      <h2 class="welcome-title">Welcome!</h2>
      <div class="pill">WE'RE GLAD TO HAVE YOU ON BOARD.</div>
      <p class="acknowledge">We acknowledge the traditional owners of the land we work on and pay our respect to their Elders both past and present.</p>
    </div>
    <div class="page">
      <div class="toc-photo" role="img" aria-label="Colleagues working together at a laptop in an office"></div>
      <div class="toc">
        <h2 class="toc-title">TABLE OF<b>CONTENT</b></h2>
        <div class="toc-rule"></div>
        <ol>
          <li><span>01.</span>EMPLOYER PLEDGE</li>
          <li><span>02.</span>MESSAGE FROM DIRECTOR</li>
          <li><span>03.</span>INTRODUCTION</li>
          <li><span>04.</span>OUR STORY</li>
          <li><span>05.</span>OUR MISSION</li>
          <li><span>06.</span>OUR VALUES</li>
          <li><span>07.</span>OUR GOALS</li>
        </ol>
        <ul>
          <li>a) ORGANISATIONAL STRUCTURE</li>
          <li>b) YOUR TEAM</li>
          <li>c) YOUR ROLE</li>
          <li>d) YOUR TRAINING PLAN</li>
          <li>e) POLICIES</li>
          <li>f) INDUCTION CHECKLIST</li>
          <li>g) SYSTEMS &amp; TOOLS</li>
        </ul>
      </div>
    </div>
  </div>
</section>

<section class="band band-pledge">
  <div class="spread" style="top:80px">
    <div class="page page-left">
      <div class="pledge-photo" role="img" aria-label="Young man working at a desk"></div>
      <div class="pledge-text">
        <h2>Our pledge to be an<strong>'Employer of Choice'</strong></h2>
        <p>We care about you! You matter. Your family and those who care for you matter.</p>
        <p>Your emotional, physical, spiritual and psychological needs are important to us.</p>
        <p>Giving you opportunity for training, skill development and career progression is important to us.</p>
        <p>We will listen to you. We will give you constructive feedback.</p>
        <p>We will support you based on your needs and goals.</p>
        <p>Your wellbeing inspires us to grow, learn and improve.</p>
      </div>
      <div class="footer-bar">www.marlowecare.com</div>
    </div>
    <div class="page page-right director">
      <div class="director-photo" role="img" aria-label="Portrait of the director"></div>
      <div class="pill">JESS ARLEN</div>
      <p class="director-role">Director<br>Marlowe Care</p>
      <div class="director-msg">
        <h2>Message from the<br>Director</h2>
        <p class="lead">Welcome to Marlowe Care! We are thrilled to have you join our team. We do some amazing, exciting &amp; challenging work here, and we are hopeful that your talent, enthusiasm, and fresh ideas will help take us to a new level!</p>
        <p class="small">We hope that you find this handbook useful. We welcome any suggestions and comments you may have, so please don't hesitate to ask any questions. I'm sure you will find your role rewarding, and we look forward to working with you as we keep choice and control at the heart of everything we do. We hope you enjoy this journey as much as we will.</p>
        <p class="small">- Jess</p>
      </div>
      <div class="page-tag">04</div>
      <div class="footer-bar">www.marlowecare.com</div>
    </div>
  </div>
</section>

<section class="band band-back">
  <div class="spread" style="top:80px">
    <div class="page back">
      <div class="brand"><span class="brand-dot"></span>Marlowe Care</div>
      <div class="contacts">
        <span><svg viewBox="0 0 10 10"><path d="M5 0a3.5 3.5 0 0 0-3.5 3.5C1.5 6 5 10 5 10s3.5-4 3.5-6.5A3.5 3.5 0 0 0 5 0z" fill="#c8ad3a"/></svg>4/22 Finch Street HARTWELL NSW 2600</span>
        <span><svg viewBox="0 0 10 10"><rect x="0.5" y="2" width="9" height="6" fill="#c8ad3a"/><path d="M.5 2l4.5 3.5L9.5 2" stroke="#fff" fill="none"/></svg>hello@marlowecare.com.au</span>
        <span><svg viewBox="0 0 10 10"><circle cx="5" cy="5" r="4.5" fill="#c8ad3a"/></svg>www.marlowecare.com</span>
        <span><svg viewBox="0 0 10 10"><path d="M2 .5l2 2-1 1.5c.8 1.5 1.5 2.2 3 3L7.5 6l2 2-1.5 1.5C4.5 9 1 5.5.5 2z" fill="#c8ad3a"/></svg>0400 000 123</span>
      </div>
    </div>
    <div class="cover" style="position:relative;box-shadow:none">
      <div class="cover-photo" role="img" aria-label="Team members stacking hands together"></div>
      <div class="cover-photo-top" role="img" aria-label="Team photo detail"></div>
      <div class="brand"><span class="brand-dot"></span>Marlowe Care</div>
      <h1 class="cover-title">Induction<br>Guide</h1>
      <div class="pill"><span>A practical guide to your<br>employment journey</span><svg width="34" height="10" viewBox="0 0 34 10"><path d="M0 5H31M26 1l5 4-5 4" stroke="#1f1f1f" stroke-width="1.4" fill="none"/></svg></div>
    </div>
  </div>
</section>

</body>
</html>
```